LVP Roofing- Bold Web Design Project

We need a website design for a company that constructs and repairs commercial and residential roofing. They need a website design that looks clean, cutting edge, and can keep up with their competitors websites (Norvelle Crest, Fenwright Roofing Company, TZL Construction). They want to look experienced and "big" enough to handle large commercial projects. They also are striving for a professional and educational feel, and want to really articulate that they work with both residential/HOA and commercial clientele. They want a high conversion rate to their social media platforms and to another area of the site where they can fill out a form, so those areas should be emphasized.

Target Market(s)

Men and Women mainly between 25 and 65, typically in the higher income bracket (200,000+).

Industry/Entity Type

Residential

Requirements
Must have
• Landing page must have two separate but equally prominent buttons, directing the customers to a specific area of the site based on their need: commercial or residential. Clicking ether of these links will lead them to a welcome page for residential customers, or a welcome page for commercial clients.
-So must have 2 pages, a landing page and a welcome page that can be adapted for use as the commercial page and the residential page.
- A photo slider on the landing page
Nice to have
• -Color scheme should generally follow along with the colors used in the logo
-Professional, bold and modern.
Should not have
• -Avoid the "mom and pop" look
-Avoid the color red in the color scheme

```html
<!DOCTYPE html>
<html lang="en">
<head>
<meta charset="utf-8">
<title>LVP Roofing</title>
<link href="https://fonts.googleapis.com/css2?family=PT+Sans:wght@400;700&family=Arimo:wght@400;700&display=swap" rel="stylesheet">
<style>
:root{
  --green:#8cb521;
  --green-dark:#5f8511;
  --green-deep:#4f720c;
  --ink:#2b2b2b;
  --text:#555;
  --muted:#8a8a8a;
  --line:#dcdcdc;
  --badge:#d6d6d6;
}
*{box-sizing:border-box;margin:0;padding:0}
html,body{width:1002px;height:1200px;overflow:hidden}
body{background:linear-gradient(#e8efd6 0,#f6f8ef 200px,#f8f8f8 600px);font-family:"Arimo",Arial,sans-serif;color:var(--text);position:relative}
.site{position:absolute;left:85px;top:15px;width:826px;height:1129px;background:#fff;border-radius:6px;box-shadow:0 0 10px rgba(0,0,0,.08);overflow:hidden}
.abs{position:absolute}
.heading{font-family:"PT Sans",sans-serif}

/* header */
.header{left:0;top:0;width:826px;height:101px;background:linear-gradient(#fff,#f1f1f1)}
.brand{left:20px;top:36px;display:flex;align-items:center;gap:8px}
.brand-mark{width:12px;height:12px;background:var(--green)}
.brand-name{font-family:"PT Sans",sans-serif;font-weight:700;font-size:25px;color:var(--ink)}
.brand-sub{left:27px;top:82px;font-size:6px;color:#333;letter-spacing:.3px}
.contractor{left:474px;top:59px;display:flex;align-items:center;gap:7px;font-family:"PT Sans",sans-serif;font-size:12px;color:#333}
.header-divider{left:640px;top:30px;width:1px;height:50px;background:var(--line)}
.callout{left:667px;top:39px;font-family:"PT Sans",sans-serif;font-size:10px;color:#333}
.callout em{font-style:normal;color:var(--green)}
.phone{left:661px;top:56px;display:flex;align-items:center;gap:5px;font-family:"PT Sans",sans-serif;font-weight:700;font-size:20px;color:#222}

/* nav */
.nav{left:0;top:101px;width:826px;height:37px;display:flex;background:linear-gradient(#a6cc35,#84ad1c)}
.nav a{display:flex;align-items:center;justify-content:center;font-family:"PT Sans",sans-serif;font-size:13px;color:#fff;text-decoration:none;border-right:1px solid rgba(255,255,255,.25)}
.nav a:last-child{border-right:0}
.nav a.active{background:linear-gradient(#7ea41b,#5e840f)}

/* hero */
.hero{left:0;top:138px;width:826px;height:296px;background:linear-gradient(90deg,#55663c 0%,#6e6d62 25%,#5c5852 55%,#3a3934 80%,#2d2c29 100%)}
.hero-shade{left:520px;top:138px;width:306px;height:296px;background:linear-gradient(90deg,rgba(0,0,0,0),rgba(0,0,0,.35))}
.hero-title{left:553px;top:182px;font-family:"PT Sans",sans-serif;font-weight:700;font-size:15px;line-height:21px;color:#fff}
.hero-list{left:556px;top:256px;list-style:none}
.hero-list li{display:flex;align-items:center;gap:8px;height:24px;font-family:"PT Sans",sans-serif;font-size:10.5px;color:#e2e2e2}
.btn{display:flex;align-items:center;justify-content:space-between;padding:0 8px 0 14px;border-radius:4px;background:linear-gradient(#9bc52e,#6a9414);color:#fff;font-family:"PT Sans",sans-serif;font-weight:700;font-size:15px;text-decoration:none}
.btn-circle{width:20px;height:20px;border-radius:50%;background:#4c6e0c;display:flex;align-items:center;justify-content:center}
.readmore{left:558px;top:365px;width:131px;height:32px}
.notch{left:29px;top:411px;width:0;height:0;border-left:19px solid transparent;border-right:19px solid transparent;border-bottom:23px solid #f0f0f0}

/* segments */
.segment{top:434px;height:98px;background:linear-gradient(#fafafa,#e4e4e4)}
.segment.commercial{left:0;width:421px;border-right:1px solid #cfcfcf}
.segment.residential{left:422px;width:404px;background:linear-gradient(#fbfbfb,#ececec)}
.segment-icon{left:29px;top:23px}
.segment h2{position:absolute;left:95px;top:20px;font-family:"PT Sans",sans-serif;font-size:20px;font-weight:400;color:#333}
.segment p{position:absolute;left:96px;top:45px;width:290px;font-size:10px;line-height:12px;color:#222}
.residential h2{left:85px}
.residential p{left:86px}

/* intro */
.intro-title{left:29px;top:559px;font-size:15px;color:#222}
.intro-text{left:29px;top:580px;width:470px;font-size:9.5px;line-height:12px}
.benefits{left:29px;top:624px;width:492px;list-style:none}
.benefits li{position:relative;padding-left:22px}
.benefits .tick{position:absolute;left:5px;top:0}
.benefits h3{font-family:"PT Sans",sans-serif;font-size:11px;color:#222;line-height:14px}
.benefits p{font-size:9.5px;line-height:12px;color:#666}

/* certified */
.certified{left:26px;top:854px;width:509px;height:102px;border:1px solid #ececec;border-radius:4px;background:linear-gradient(#f7f7f7,#fff)}
.cert-badge{position:absolute;left:45px;top:21px;width:60px;height:60px;border-radius:50%;background:var(--badge)}
.certified p{position:absolute;left:147px;top:22px;width:350px;font-size:9.5px;line-height:12px;color:#666}

/* sidebar */
.ribbon{left:558px;top:560px;width:252px;height:33px;background:linear-gradient(#9ec933,#77a115);color:#fff;font-family:"PT Sans",sans-serif;font-weight:700;font-size:14px;display:flex;align-items:center;justify-content:center}
.ribbon-fold{top:593px;width:0;height:0;border-top:6px solid var(--green-deep)}
.ribbon-fold.left{left:558px;border-left:7px solid transparent}
.ribbon-fold.right{left:803px;border-right:7px solid transparent}
.form-box{left:565px;top:593px;width:235px;height:231px;border:1px solid #e2e2e2;border-top:0;border-radius:0 0 4px 4px;background:#fff}
.field{position:absolute;left:18px;width:199px;height:27px;border:1px solid #d8d8d8;background:#fff;font-size:9.5px;color:#555;display:flex;align-items:center;padding-left:8px}
.label{position:absolute;left:18px;top:120px;font-family:"PT Sans",sans-serif;font-size:10px;font-weight:700;color:#333}
.select-arrow{position:absolute;right:-1px;top:-1px;width:28px;height:27px;background:linear-gradient(#9ec933,#6f9a13);display:flex;align-items:center;justify-content:center}
.confirm{left:51px;top:181px;width:131px;height:32px}

.testi-title{left:560px;top:843px;font-size:15px;color:#222}
.testi{left:558px;top:869px;width:251px;height:74px;background:#f4f4f4;border-radius:4px;padding:10px 11px}
.testi p{font-size:9.5px;line-height:12px;color:#666}
.testi cite{display:block;margin-top:5px;font-size:9.5px;color:var(--green);font-style:italic}
.testi cite b{font-style:normal}
.testi-tail{left:580px;top:943px;width:0;height:0;border-top:11px solid #f4f4f4;border-right:16px solid transparent}

/* footer */
.footer{left:0;top:978px;width:826px;height:151px;background:linear-gradient(#81a91c,#5c820f);border-radius:0 0 6px 6px}
.footer-contact{left:41px;top:1039px;font-family:"PT Sans",sans-serif;font-size:9.5px;line-height:12px;color:#fff}
.footer-contact i{font-style:italic}
.footer-divider{left:382px;top:998px;width:1px;height:110px;background:rgba(255,255,255,.15);box-shadow:1px 0 0 rgba(0,0,0,.08)}
.footer-badge{left:424px;top:1030px;width:56px;height:56px;border-radius:50%;background:rgba(255,255,255,.3)}
.footer-claim{left:504px;top:1042px;font-family:"PT Sans",sans-serif;font-size:14px;line-height:18px;color:#fff}

.copyright{position:absolute;left:0;top:1165px;width:1002px;text-align:center;font-size:8px;color:var(--muted)}
</style>
</head>
<body>
<div class="site">
  <header class="header abs"></header>
  <div class="brand abs"><span class="brand-mark"></span><span class="brand-name">LVP Network</span></div>
  <div class="brand-sub abs">CONSTRUCTION &amp; DISASTER MANAGEMENT</div>
  <div class="contractor abs">
    <svg width="22" height="16" viewBox="0 0 22 16"><path d="M2 13 Q2 2 11 2 Q20 2 20 13 Z" fill="#f2c21d"/><rect x="0" y="12" width="22" height="3" rx="1.5" fill="#d9a40f"/></svg>
    Full Service Contractor
  </div>
  <div class="header-divider abs"></div>
  <div class="callout abs">Call today for a <em>FREE</em> estimate!</div>
  <div class="phone abs">
    <svg width="16" height="16" viewBox="0 0 16 16"><circle cx="8" cy="8" r="8" fill="#8cb521"/><path d="M4 6 Q8 3 12 6 L11 8 L9 7 L9 6 L7 6 L7 7 L5 8 Z M5 9 h6 v3 h-6z" fill="#fff"/></svg>
    (555) 017-4410
  </div>

  <nav class="nav abs">
    <a class="active" href="#" style="width:85px">Home</a>
    <a href="#" style="width:104px">About Us</a>
    <a href="#" style="width:102px">Services</a>
    <a href="#" style="width:197px">Insurance &amp; Storm Damage</a>
    <a href="#" style="width:110px">Ventilation</a>
    <a href="#" style="width:102px">Products</a>
    <a href="#" style="width:126px">Contact Us</a>
  </nav>

  <div class="hero abs" role="img" aria-label="Slider photo of a large grey two-storey house with dormers and a stone chimney among trees"></div>
  <div class="hero-shade abs"></div>
  <div class="hero-title abs">Construction &amp; Disaster<br>Management for Commercial</div>
  <ul class="hero-list abs">
    <li><svg width="13" height="13" viewBox="0 0 14 14"><circle cx="7" cy="7" r="7" fill="#8cb521"/><path d="M3.5 7.2 L6 9.5 L10.5 4.5" stroke="#fff" stroke-width="1.8" fill="none"/></svg>Cellar Membrane Waterproofing</li>
    <li><svg width="13" height="13" viewBox="0 0 14 14"><circle cx="7" cy="7" r="7" fill="#8cb521"/><path d="M3.5 7.2 L6 9.5 L10.5 4.5" stroke="#fff" stroke-width="1.8" fill="none"/></svg>Commercial Roofing</li>
    <li><svg width="13" height="13" viewBox="0 0 14 14"><circle cx="7" cy="7" r="7" fill="#8cb521"/><path d="M3.5 7.2 L6 9.5 L10.5 4.5" stroke="#fff" stroke-width="1.8" fill="none"/></svg>Conservatory Roof</li>
    <li><svg width="13" height="13" viewBox="0 0 14 14"><circle cx="7" cy="7" r="7" fill="#8cb521"/><path d="M3.5 7.2 L6 9.5 L10.5 4.5" stroke="#fff" stroke-width="1.8" fill="none"/></svg>Conservatory Roof Seals</li>
  </ul>
  <a class="btn readmore abs" href="#">Readmore <span class="btn-circle"><svg width="8" height="9" viewBox="0 0 8 9"><path d="M1 0 L8 4.5 L1 9Z" fill="#fff"/></svg></span></a>
  <div class="notch abs"></div>

  <section class="segment commercial abs">
    <svg class="segment-icon abs" width="46" height="42" viewBox="0 0 46 42"><path d="M4 14 L23 3 L42 14 Z" fill="#9aa0a6"/><rect x="7" y="14" width="32" height="22" fill="#c9ced3"/><rect x="11" y="18" width="4" height="14" fill="#7e858c"/><rect x="21" y="18" width="4" height="14" fill="#7e858c"/><rect x="31" y="18" width="4" height="14" fill="#7e858c"/><rect x="3" y="36" width="40" height="4" fill="#8d949a"/></svg>
    <h2>LVP COMMERCIAL</h2>
    <p>Lorem ipsum dolor sit amet, consectetuer adipiscing elit, sed diam nonummy nibh euismod tincidunt ut laoreet dolore magna aliquam erat volutpat.</p>
  </section>
  <section class="segment residential abs">
    <svg class="segment-icon abs" style="left:20px;top:22px" width="52" height="44" viewBox="0 0 52 44"><path d="M2 12 L18 8 L34 12 L50 8 L50 40 L34 44 L18 40 L2 44 Z" fill="#7cb342"/><path d="M18 8 L34 12 L34 44 L18 40 Z" fill="#5aa0d6"/><circle cx="26" cy="10" r="7" fill="#f07a1a"/><circle cx="26" cy="10" r="2.5" fill="#fff"/><path d="M20 13 L26 26 L32 13 Z" fill="#f07a1a"/></svg>
    <h2>LVP RESIDENTAL</h2>
    <p>Lorem ipsum dolor sit amet, consectetuer adipiscing elit, sed diam nonummy nibh euismod tincidunt ut laoreet dolore magna aliquam erat volutpat.</p>
  </section>

  <h2 class="intro-title heading abs">LVP Roofing &amp; Construction</h2>
  <p class="intro-text abs">LVP Roofing was founded on the principles of honesty and integrity. We have many years of building experience – including new construction and home remodel, with a primary focus on roofing and siding.</p>
  <ul class="benefits abs">
    <li style="height:50px"><svg class="tick" width="13" height="13" viewBox="0 0 14 14"><circle cx="7" cy="7" r="7" fill="#8cb521"/><path d="M3.5 7.2 L6 9.5 L10.5 4.5" stroke="#fff" stroke-width="1.8" fill="none"/></svg><h3>Full Service Contractor</h3><p>Lorem ipsum dolor sit amet, consectetur adipisicing elit, sed do eiusmod tempor incididunt ut labore et dolore magna aliqua.</p></li>
    <li style="height:64px"><svg class="tick" width="13" height="13" viewBox="0 0 14 14"><circle cx="7" cy="7" r="7" fill="#8cb521"/><path d="M3.5 7.2 L6 9.5 L10.5 4.5" stroke="#fff" stroke-width="1.8" fill="none"/></svg><h3>We answer the phone!</h3><p>Sed ut perspiciatis unde omnis iste natus error sit voluptatem accusantium doloremque laudantium, totam rem aperiam, eaque ipsa quae ab illo inventore veritatis et quasi architecto beatae vitae dicta sunt explicabo.</p></li>
    <li style="height:50px"><svg class="tick" width="13" height="13" viewBox="0 0 14 14"><circle cx="7" cy="7" r="7" fill="#8cb521"/><path d="M3.5 7.2 L6 9.5 L10.5 4.5" stroke="#fff" stroke-width="1.8" fill="none"/></svg><h3>Storm Damage Specialist</h3><p>Nemo enim ipsam voluptatem quia voluptas sit aspernatur aut odit aut fugit, sed quia consequuntur magni dolores eos qui ratione voluptatem sequi nesciunt.</p></li>
    <li><svg class="tick" width="13" height="13" viewBox="0 0 14 14"><circle cx="7" cy="7" r="7" fill="#8cb521"/><path d="M3.5 7.2 L6 9.5 L10.5 4.5" stroke="#fff" stroke-width="1.8" fill="none"/></svg><h3>Assistance with your insurance claim process</h3><p>Neque porro quisquam est, qui dolorem ipsum quia dolor sit amet, consectetur, adipisci velit, sed quia non numquam eius modi tempora incidunt ut labore et dolore magnam aliquam quaerat voluptatem.</p></li>
  </ul>

  <div class="certified abs">
    <div class="cert-badge" role="img" aria-label="Certification badge"></div>
    <p>LVP Roofing is a full-service Verilon certified roofing contractor with years of experience in all areas of roofing and construction services. We offer 24 hour emergency roofing repair service. You can count on LVP Roofing for speedy reliable service when you need it most. No job too big or to small. We offer affordable solutions for everyone.</p>
  </div>

  <div class="ribbon abs">Serving the greater Kansas City area</div>
  <div class="ribbon-fold left abs"></div>
  <div class="ribbon-fold right abs"></div>
  <form class="form-box abs">
    <div class="field" style="top:17px">First Name</div>
    <div class="field" style="top:51px">Last Name</div>
    <div class="field" style="top:84px">E-mail</div>
    <div class="label">Location</div>
    <div class="field" style="top:138px">Gladstone<span class="select-arrow"><svg width="8" height="5" viewBox="0 0 8 5"><path d="M0 0 H8 L4 5Z" fill="#fff"/></svg></span></div>
    <a class="btn confirm abs" href="#">Confirmed <span class="btn-circle"><svg width="8" height="9" viewBox="0 0 8 9"><path d="M1 0 L8 4.5 L1 9Z" fill="#fff"/></svg></span></a>
  </form>

  <h2 class="testi-title heading abs">Testimonials</h2>
  <blockquote class="testi abs">
    <p>Lorem ipsum dolor sit amet, consectetur adipisicing elit, sed do eiusmod tempor incididunt ut labore et dolore magna aliqua.</p>
    <cite>Daniel, <b>Smithville</b></cite>
  </blockquote>
  <div class="testi-tail abs"></div>

  <footer class="footer abs"></footer>
  <div class="footer-contact abs">LVP Roofing Kansas City, MO (555) 014-2288 / Fax (555) 014-2290<br>Email : <i>office@lvproofing.example</i></div>
  <div class="footer-divider abs"></div>
  <div class="footer-badge abs" role="img" aria-label="Warranty badge"></div>
  <div class="footer-claim abs">We offer around the clock emergency service<br>for unexpected emergencies!</div>
</div>
<div class="copyright">Copyright © 2011 LVP Network, All right reserved.</div>
</body>
</html>
```